Beautiful Web banner ad 300X250

i need an animated banner with graphics, to drive traffic to a website that focuses on architecturally significant homes in Toronto.

"crisp metro dwellings" logo should appear, and visuals. Call to action is "tour the latest homes"

http://brentolsvik.com

Number of Pages Required

1 page

Font styles to use
Sans Serif

Requirements
Must have
• the logo of my brand
Nice to have
• smart graphics, nice transitions, elegant

```html
<!DOCTYPE html>
<html lang="en">
<head>
<meta charset="utf-8">
<title>Crisp Metro Dwellings – Banner Set</title>
<link rel="stylesheet" href="https://fonts.googleapis.com/css2?family=Open+Sans:wght@400;600;700;800&display=swap">
<style>
  :root {
    --stage: #2a1710;
    --navy: #0d3a80;
    --navy-deep: #0a2f6a;
    --orange: #f7941e;
    --orange-light: #fbac45;
    --white: #ffffff;
    --band: #e6e8ec;
    --border: #0b0b0b;
  }
  html, body {
    margin: 0;
    padding: 0;
    width: 1200px;
    height: 677px;
    overflow: hidden;
    background: var(--stage);
    font-family: "Open Sans", Arial, sans-serif;
  }
  .stage {
    position: relative;
    width: 1200px;
    height: 677px;
    background:
      radial-gradient(ellipse 60% 70% at 50% 40%, rgba(90,45,25,0.35), transparent 70%),
      var(--stage);
  }
  .banner {
    position: absolute;
    width: 288px;
    height: 239px;
    background: var(--navy);
    border: 1px solid var(--border);
    box-sizing: border-box;
    overflow: hidden;
    color: var(--white);
  }
  .banner--1 { left: 111px; top: 90px; }
  .banner--2 { left: 412px; top: 90px; }
  .banner--3 { left: 713px; top: 90px; }
  .banner--4 { left: 261px; top: 344px; }
  .banner--5 { left: 566px; top: 344px; }

  .banner__headline {
    position: absolute;
    left: 0; right: 0; top: 4px;
    margin: 0;
    text-align: center;
    font-size: 20px;
    font-weight: 800;
    letter-spacing: -0.4px;
    text-transform: uppercase;
    line-height: 26px;
    white-space: nowrap;
  }
  .banner__city {
    position: absolute;
    left: 97px; top: 26px;
    width: 94px; height: 16px;
    background: var(--orange);
    font-size: 13px;
    line-height: 16px;
    text-align: center;
    text-transform: uppercase;
  }
  .banner__intro {
    position: absolute;
    left: 0; right: 0; top: 46px;
    margin: 0;
    text-align: center;
    font-size: 13.5px;
    line-height: 15px;
  }
  .banner__photo {
    position: absolute;
    left: 0; right: 0; top: 84px;
    height: 116px;
  }
  .banner__photo--kitchen {
    background:
      linear-gradient(180deg, transparent 55%, rgba(245,243,238,0.9) 80%, #f4f2ee 100%),
      linear-gradient(90deg, #1f3560 0%, #3d5a8c 14%, #2c3440 24%, #d8d6d0 32%, #eeeae4 55%, #bfb7ac 72%, #e9e6e0 88%, #6b5a4a 100%);
  }
  .banner__photo--living {
    background:
      linear-gradient(180deg, transparent 50%, rgba(140,80,40,0.0) 60%, rgba(150,85,40,0.75) 100%),
      linear-gradient(90deg, #9c978f 0%, #d9d6d0 22%, #f7f6f3 42%, #e2ddd5 58%, #ffffff 70%, #cdbfae 84%, #7a4a2c 100%);
  }
  .banner__photo--facade {
    background:
      linear-gradient(180deg, transparent 60%, rgba(95,110,60,0.7) 100%),
      linear-gradient(90deg, #eef1ee 0%, #dfe3da 25%, #b9b49a 42%, #8c8466 58%, #5d6a3e 72%, #3e4a2c 86%, #6c7550 100%);
  }
  .banner__photo--townhouse {
    background:
      linear-gradient(90deg, transparent 35%, rgba(160,125,85,0.85) 45%, rgba(120,90,60,0.9) 70%, transparent 82%),
      linear-gradient(180deg, #4d6fa6 0%, #6e8fc2 35%, #3a4d6c 62%, #23262b 85%, #15171a 100%);
  }
  .banner__photo--library {
    background:
      linear-gradient(180deg, transparent 60%, rgba(150,95,50,0.7) 100%),
      linear-gradient(90deg, #f1eee8 0%, #e0d7c6 18%, #f3efe8 32%, #cdb99a 46%, #efe8dc 60%, #9a6a3e 74%, #3b2a20 88%, #a26b3b 100%);
  }

  .banner__curve {
    position: absolute;
    left: 0; top: 82px;
    width: 288px; height: 40px;
  }
  .banner__logo {
    position: absolute;
    left: 0; top: 173px;
    width: 154px; height: 27px;
    background: var(--navy-deep);
  }
  .banner__logo-mark {
    position: absolute;
    left: 4px; top: 8px;
    width: 13px; height: 8px;
    background: var(--white);
  }
  .banner__logo-name {
    position: absolute;
    left: 21px; top: 0;
    font-size: 16.5px;
    line-height: 18px;
    font-weight: 400;
    letter-spacing: -0.3px;
    color: var(--white);
  }
  .banner__logo-tag {
    position: absolute;
    left: 44px; top: 17px;
    font-size: 7.5px;
    line-height: 9px;
    font-weight: 400;
    color: var(--white);
    white-space: nowrap;
  }
  .banner__band {
    position: absolute;
    left: 0; right: 0; top: 200px; bottom: 0;
    background: linear-gradient(90deg, #dcdfe4, var(--band) 40%, #f3f4f6 100%);
  }
  .banner__cta {
    position: absolute;
    left: 37px; top: 204px;
    width: 216px; height: 31px;
    border-radius: 16px;
    background: linear-gradient(180deg, var(--orange-light), var(--orange));
    color: var(--white);
    font-size: 14px;
    font-weight: 700;
    line-height: 31px;
    text-align: center;
    text-transform: uppercase;
    letter-spacing: -0.3px;
    white-space: nowrap;
    box-shadow: 0 1px 2px rgba(0,0,0,0.25);
  }
  .banner__cta-arrow {
    display: inline-block;
    width: 0; height: 0;
    margin-left: 8px;
    border-top: 5px solid transparent;
    border-bottom: 5px solid transparent;
    border-left: 8px solid var(--white);
    vertical-align: 0;
  }
</style>
</head>
<body>
<main class="stage">

  <section class="banner banner--1">
    <div class="banner__photo banner__photo--kitchen" role="img" aria-label="Modern kitchen and dining room with a city skyline view at dusk"></div>
    <svg class="banner__curve" viewBox="0 0 288 40" aria-hidden="true"><path d="M0 0 H288 V8 Q150 -2 40 22 L30 14 L0 26 Z" fill="#0d3a80"/></svg>
    <h2 class="banner__headline">Crisp Metro Dwellings</h2>
    <div class="banner__city">In Toronto</div>
    <p class="banner__intro">From modern homes to restored<br>victorians and vintage lofts.</p>
    <div class="banner__logo"><span class="banner__logo-mark"></span><span class="banner__logo-name">brentolsvik.com</span><span class="banner__logo-tag">crisp metro dwellings</span></div>
    <div class="banner__band"></div>
    <div class="banner__cta">Tour the latest homes<span class="banner__cta-arrow"></span></div>
  </section>

  <section class="banner banner--2">
    <div class="banner__photo banner__photo--living" role="img" aria-label="Bright open-plan living room with large windows and wood floors"></div>
    <svg class="banner__curve" viewBox="0 0 288 40" aria-hidden="true"><path d="M0 0 H288 V8 Q150 -2 40 22 L30 14 L0 26 Z" fill="#0d3a80"/></svg>
    <h2 class="banner__headline">Crisp Metro Dwellings</h2>
    <div class="banner__city">In Toronto</div>
    <p class="banner__intro">From modern homes to restored<br>victorians and vintage lofts.</p>
    <div class="banner__logo"><span class="banner__logo-mark"></span><span class="banner__logo-name">brentolsvik.com</span><span class="banner__logo-tag">crisp metro dwellings</span></div>
    <div class="banner__band"></div>
    <div class="banner__cta">Tour the latest homes<span class="banner__cta-arrow"></span></div>
  </section>

  <section class="banner banner--3">
    <div class="banner__photo banner__photo--facade" role="img" aria-label="Stacked modern townhouses with green planted terraces"></div>
    <svg class="banner__curve" viewBox="0 0 288 40" aria-hidden="true"><path d="M0 0 H288 V8 Q150 -2 40 22 L30 14 L0 26 Z" fill="#0d3a80"/></svg>
    <h2 class="banner__headline">Crisp Metro Dwellings</h2>
    <div class="banner__city">In Toronto</div>
    <p class="banner__intro">From modern homes to restored<br>victorians and vintage lofts.</p>
    <div class="banner__logo"><span class="banner__logo-mark"></span><span class="banner__logo-name">brentolsvik.com</span><span class="banner__logo-tag">crisp metro dwellings</span></div>
    <div class="banner__band"></div>
    <div class="banner__cta">Tour the latest homes<span class="banner__cta-arrow"></span></div>
  </section>

  <section class="banner banner--4">
    <div class="banner__photo banner__photo--townhouse" role="img" aria-label="Contemporary townhouse building lit at twilight"></div>
    <svg class="banner__curve" viewBox="0 0 288 40" aria-hidden="true"><path d="M0 0 H288 V8 Q150 -2 40 22 L30 14 L0 26 Z" fill="#0d3a80"/></svg>
    <h2 class="banner__headline">Crisp Metro Dwellings</h2>
    <div class="banner__city">In Toronto</div>
    <p class="banner__intro">From modern homes to restored<br>victorians and vintage lofts.</p>
    <div class="banner__logo"><span class="banner__logo-mark"></span><span class="banner__logo-name">brentolsvik.com</span><span class="banner__logo-tag">crisp metro dwellings</span></div>
    <div class="banner__band"></div>
    <div class="banner__cta">Tour the latest homes<span class="banner__cta-arrow"></span></div>
  </section>

  <section class="banner banner--5">
    <div class="banner__photo banner__photo--library" role="img" aria-label="Loft interior with floor-to-ceiling bookshelves and an open wooden staircase"></div>
    <svg class="banner__curve" viewBox="0 0 288 40" aria-hidden="true"><path d="M0 0 H288 V8 Q150 -2 40 22 L30 14 L0 26 Z" fill="#0d3a80"/></svg>
    <h2 class="banner__headline">Crisp Metro Dwellings</h2>
    <div class="banner__city">In Toronto</div>
    <p class="banner__intro">From modern homes to restored<br>victorians and vintage lofts.</p>
    <div class="banner__logo"><span class="banner__logo-mark"></span><span class="banner__logo-name">brentolsvik.com</span><span class="banner__logo-tag">crisp metro dwellings</span></div>
    <div class="banner__band"></div>
    <div class="banner__cta">Tour the latest homes<span class="banner__cta-arrow"></span></div>
  </section>

</main>
</body>
</html>
```